Business Card for Tutoring Company

We need a logo/symbol for an education company, along with an attractive business card. The logo should resemble both a pi symbol and the letter T.
Updates

Dear Designers,

I am narrowing down what I am looking for. 
I want the front of the card to be primarily white, with the company name "Bright Harbor Learning" positioned towards the center.  The first letter, 'T' in 'Bright' will be modified so that it resembles a Pi symbol.
My personal information will be at the bottom.  If you think it fits, the website can be strewn across the top.

As for the back of the card, it will be primarily blue.  Toward the center will be the same T/pi shape engraved into a circular disk/button/emblem shape with some border.  It should be noted that I do like shiny blue, like the blue face of a Varnel.  Underneath the logo will be white text that reads, "Making Independent Learners and Thinkers."  At the very bottom of the card in smaller white font, the website "BrightHarborLearning.example" is written.

For more clarification, see my recent attachment.

Thank you.

Leonard

Industry/Entity Type

Education

Logo styles of interest
Pictorial/Combination Logo
Requirements
Must have
• LOGO:
The logo is a solid blue circle with a symbol cutout from it. The cut out should closely resemble π and be the color white.

CARD:
The front has the logo in the top left corner, with "BRIGHT HARBOR LEARNING" written out beside it, spanning the width of the card. " At the bottom, personal information can be placed: Name, Title, Phone, Email.
The back has the the logo centered and enlarged. The website is printed "BrightHarborLearning.example
Nice to have
• LOGO:
It would be nice if the logo/pi symbol could be used as a letter T when spelling BHL or Bright Harbor Learning.

CARD:
The enlarged logo on the back of the card can be enhanced (i.e. the blue is not solid blue but shiny, like the metallic blue face of a varnel) It would also be nice if the logo had a cool background (i.e. instead of the cutout of the pi-shape being white, it could be outerspace or something. Also, a motto "Making Independent Learner and Thinkers" printed under "BrightHarborLearning.example" would be nice, if it fits.

```html
<!DOCTYPE html>
<html lang="en">
<head>
<meta charset="utf-8">
<title>Bright Harbor Learning – Business Card Front</title>
<link rel="stylesheet" href="https://fonts.googleapis.com/css2?family=Josefin+Sans:wght@300;400&family=Roboto:wght@500&display=swap">
<style>
  :root {
    --stage: #000000;
    --card: #f2f2f1;
    --brand-blue: #27339b;
    --emblem-blue: #1b2f9c;
    --ink: #111111;
    --dots: #1a1a1a;
    --label: #ffffff;
  }
  html, body {
    margin: 0;
    width: 1200px;
    height: 900px;
    overflow: hidden;
    background: var(--stage);
  }
  .stage {
    position: relative;
    width: 1200px;
    height: 900px;
  }
  .card {
    position: absolute;
    left: 68px;
    top: 125px;
    width: 1063px;
    height: 650px;
    background: linear-gradient(135deg, #f6f6f5 0%, var(--card) 55%, #ebebea 100%);
    overflow: hidden;
  }
  .card-decor {
    position: absolute;
    inset: 0;
  }
  .brand {
    position: absolute;
    left: 22px;
    top: 15px;
    display: flex;
    align-items: center;
    gap: 22px;
  }
  .brand-emblem {
    width: 224px;
    height: 224px;
    border-radius: 50%;
    background: var(--emblem-blue);
    flex: none;
  }
  .brand-name {
    font-family: "Josefin Sans", sans-serif;
    font-weight: 300;
    font-size: 50px;
    color: var(--brand-blue);
    letter-spacing: 1px;
    white-space: nowrap;
    padding-top: 36px;
  }
  .tagline {
    position: absolute;
    left: 0;
    right: 0;
    top: 295px;
    margin: 0;
    text-align: center;
    font-family: "Roboto", sans-serif;
    font-weight: 500;
    font-size: 45px;
    color: var(--ink);
    letter-spacing: 0.5px;
  }
  .tagline-rule {
    position: absolute;
    left: 300px;
    top: 385px;
    width: 490px;
    height: 4px;
    background: var(--ink);
  }
  .contact {
    position: absolute;
    right: 29px;
    top: 436px;
    margin: 0;
    text-align: right;
    font-family: "Josefin Sans", sans-serif;
    font-weight: 300;
    font-size: 37px;
    line-height: 50px;
    color: var(--ink);
    font-style: normal;
  }
  .contact span { display: block; }
  .side-label {
    position: absolute;
    right: 34px;
    bottom: 30px;
    font-family: "Roboto", sans-serif;
    font-weight: 500;
    font-size: 36px;
    color: var(--label);
  }
</style>
</head>
<body>
<div class="stage">
  <section class="card" aria-label="Business card front">
    <svg class="card-decor" width="1063" height="650" viewBox="0 0 1063 650" aria-hidden="true">
      <g stroke="var(--dots)" stroke-width="4" stroke-linecap="round" stroke-dasharray="0 11.5" fill="none">
        <line x1="821" y1="22" x2="1050" y2="22"/>
        <line x1="1038" y1="10" x2="1038" y2="112"/>
        <line x1="22" y1="540" x2="22" y2="645"/>
        <line x1="10" y1="632" x2="242" y2="632"/>
      </g>
    </svg>

    <div class="brand">
      <div class="brand-emblem" aria-hidden="true"></div>
      <div class="brand-name">BRIGHT HARBOR LEARNING</div>
    </div>

    <h1 class="tagline">PREMIER EDUCATION SERVICES</h1>
    <div class="tagline-rule"></div>

    <address class="contact">
      <span class="contact-name">Leonard Ashcombe</span>
      <span class="contact-title">Education Consultant</span>
      <span class="contact-phone">(555) 014 2876</span>
      <span class="contact-email">leonard@BHLbest.example</span>
    </address>
  </section>
  <div class="side-label">Front</div>
</div>
</body>
</html>
```